Business Cards for a company that provides webstore services to veterinarians

We need business cards designed for our main service PawCartHub. PawCartHub is a webstore that veterinarian clinics can use to that will allow their clients to purchase products for their pets. Our company is Brindlow Veterinary Solutions (BVS). Our mission statement is We love pets! We will do everything possible to facilitate along, healthy and happy relationship with their families.

Target Market(s)

Veterinarians

Industry/Entity Type

Veterinary

Contact Information for Business Card

I would like the design to incorporate the colours our our company. Cards should have room for employee name, title (only necessary in two instances), phone number, mobile number, email address and linkedin symbol and related profile name ie Marla Quinton. I would like the PawCartHub logo to appear on one side and BVS logo to appear on the other. I will need both an english and french version. I can provide the french translation. Please focus on english version and then we will translate

Colors

Designer to choose colors to be used in the design.

Requirements
Must have
• one side - PawCartHub logo with persons name, phone number, mobile number, email address
• second side - BVS logo
• colours should be consistent with our company. colours are as follows:
• Red
• RGB: 190 / 30 / 45
• CYMK: 14 / 100 / 90 /10
• Hex: #BE1E2D
• Gray
• RGB: 88 / 89 / 86
• CYMK: 3 / 2 / 0 /64
• Hex: #585956
Nice to have
• address of company - can be on either side address is 4817 Feldmoor Street Suite 305 Burlington ON K2R 6T4. Toll free number will vary depending on person
• Linkedin symbol and name of person
• on second side with BVS logo our company's mission statement
Should not have
• nothing comes to mind

```html
<!DOCTYPE html>
<html lang="en">
<head>
<meta charset="utf-8">
<title>PawCartHub Business Cards</title>
<link href="https://fonts.googleapis.com/css2?family=Open+Sans:wght@400;600;700;800&display=swap" rel="stylesheet">
<style>
  :root {
    --brand-red: #be1e2d;
    --brand-gray: #585956;
    --ink-dark: #3a3a3a;
    --paper: #ffffff;
    --backdrop: #e4e4e4;
  }
  * { margin: 0; padding: 0; box-sizing: border-box; }
  html, body { width: 1200px; height: 900px; overflow: hidden; }
  body {
    background: var(--backdrop);
    font-family: "Open Sans", Arial, sans-serif;
    position: relative;
  }
  .card {
    position: absolute;
    left: 250px;
    width: 700px;
    height: 400px;
    background: var(--paper);
    box-shadow: 0 6px 18px rgba(0,0,0,0.18);
    overflow: hidden;
  }
  .card--company { top: 40px; }
  .card--contact { top: 460px; }

  /* Company side */
  .company-mark {
    position: absolute;
    top: 92px; left: 0; width: 100%;
    display: flex; flex-direction: column; align-items: center;
  }
  .company-mark__dot {
    width: 56px; height: 56px; border-radius: 50%;
    background: var(--brand-red);
    margin-bottom: 16px;
  }
  .company-mark__name {
    font-weight: 700; font-size: 30px; line-height: 1.1;
    color: var(--brand-red);
  }
  .mission { margin-top: 22px; text-align: center; }
  .mission__label {
    font-size: 18px; font-weight: 800; color: var(--brand-red); line-height: 1.3;
  }
  .mission__text {
    font-size: 18px; font-weight: 700; color: var(--ink-dark); line-height: 1.3;
  }

  /* Contact side */
  .swoosh { position: absolute; inset: 0; }
  .store-name {
    position: absolute; left: 60px; top: 168px;
    font-size: 44px; font-weight: 600; color: var(--brand-gray);
    letter-spacing: -0.5px;
  }
  .contact-block {
    position: absolute; right: 22px; top: 88px;
    color: var(--paper); text-align: right;
  }
  .contact-block__name { font-size: 17px; font-weight: 700; line-height: 1.2; }
  .contact-block__title { font-size: 16px; font-weight: 400; margin-bottom: 4px; }
  .contact-line {
    display: flex; justify-content: flex-end; align-items: center; gap: 10px;
    font-size: 15px; line-height: 23px;
  }
  .contact-line svg { width: 13px; height: 13px; flex: none; }
  .profile {
    position: absolute; left: 46px; bottom: 10px;
    display: flex; align-items: center; gap: 8px;
    color: var(--paper); font-size: 16px;
  }
  .profile__square { width: 14px; height: 14px; background: var(--paper); }
</style>
</head>
<body>

<section class="card card--company">
  <div class="company-mark">
    <div class="company-mark__dot"></div>
    <div class="company-mark__name">Brindlow Veterinary Solutions</div>
    <div class="mission">
      <div class="mission__label">MISSION STATEMENT</div>
      <div class="mission__text">We love pets!</div>
    </div>
  </div>
</section>

<section class="card card--contact">
  <svg class="swoosh" viewBox="0 0 700 400" preserveAspectRatio="none">
    <path d="M460,0 C535,150 430,330 0,368 L0,400 L700,400 L700,0 Z" fill="var(--brand-red)"/>
    <path d="M438,0 C505,150 410,325 0,356" fill="none" stroke="var(--brand-red)" stroke-width="2"/>
  </svg>

  <div class="store-name">PawCartHub</div>

  <div class="contact-block">
    <div class="contact-block__name">MARLA QUINTON</div>
    <div class="contact-block__title">CEO/Founder</div>
    <div class="contact-line">689 555 0142
      <svg viewBox="0 0 16 16"><path d="M3 1h3l1 4-2 1c1 2 3 4 5 5l1-2 4 1v3c0 1-1 2-2 2C7 15 1 9 1 3c0-1 1-2 2-2z" fill="#fff"/></svg>
    </div>
    <div class="contact-line">836 555 0178
      <svg viewBox="0 0 16 16"><rect x="4" y="1" width="8" height="14" rx="1.5" fill="none" stroke="#fff" stroke-width="1.6"/><circle cx="8" cy="12.5" r="0.9" fill="#fff"/></svg>
    </div>
    <div class="contact-line">marla@pawcarthub
      <svg viewBox="0 0 16 16"><rect x="1" y="3" width="14" height="10" fill="#fff"/><path d="M1 3l7 5 7-5" fill="none" stroke="var(--brand-red)" stroke-width="1.3"/></svg>
    </div>
    <div class="contact-line">www.pawcarthub
      <svg viewBox="0 0 16 16"><circle cx="8" cy="8" r="6.5" fill="none" stroke="#fff" stroke-width="1.5"/><path d="M1.5 8h13M8 1.5c-3 3.5-3 9.5 0 13M8 1.5c3 3.5 3 9.5 0 13" fill="none" stroke="#fff" stroke-width="1.1"/></svg>
    </div>
  </div>

  <div class="profile">
    <span class="profile__square"></span>
    <span>Marla Quinton</span>
  </div>
</section>

</body>
</html>
```